Kelvora Template

Hi Guys,

I have just completed a logo design with Vantelo Works and I am very happy with what I have seen so far. Next I would like to create a template for the site that will be skinned into a DNN skin.

Our goal with Kelvora is to create a site were people can register and buy a e-commerce site from us. The site needs to match the logo color scheme and entice people to register. The site needs to be clear on what they are receiving and make sure that the registration process is easily accessible. our target market is the Joe Soup's that want to create an online presence and sell their products.

I'm excited to see what you guys are going to come up with.

Regards

Willem

Hi all,

Thank you for your inputs, It was hard to choose a template as I feel that so many of them where so good.

Well done.

Regards

Willem Badenhorst

```html
<!DOCTYPE html>
<html lang="en">
<head>
<meta charset="utf-8">
<title>Kelvora – Build Your Online Store</title>
<link rel="stylesheet" href="https://fonts.googleapis.com/css2?family=Open+Sans:wght@300;400;600;700&family=Oswald:wght@400;500&family=Lobster&display=swap">
<style>
:root{
  --navy:#0c2a62;
  --navy-deep:#071d47;
  --blue:#1a4c9c;
  --sky:#4cc3f5;
  --orange:#ef6a1f;
  --orange-dark:#d9540f;
  --paper:#ededed;
  --ink:#1e2b45;
  --grey:#6b6f76;
  --white:#ffffff;
}
*{box-sizing:border-box;margin:0;padding:0}
html,body{width:1200px;height:2162px;overflow:hidden}
body{position:relative;font-family:"Open Sans",Arial,sans-serif;color:var(--ink);background:var(--white)}
.abs{position:absolute}

/* Header */
.site-header{left:0;top:0;width:1200px;height:82px;background:var(--white);border-bottom:1px solid #dfe3ea}
.brand{left:177px;top:20px;display:flex;align-items:center;gap:10px}
.brand-mark{width:30px;height:30px;background:var(--navy)}
.brand-name{font-family:"Open Sans",sans-serif;font-weight:700;font-size:34px;color:var(--navy);letter-spacing:-0.5px}
.main-nav{left:525px;top:30px;display:flex;gap:0}
.main-nav a{display:block;font-family:"Oswald",sans-serif;font-size:15px;color:var(--navy);text-decoration:none;padding:4px 16px;margin-right:16px;border-radius:4px}
.main-nav a.active{background:var(--navy);color:var(--white);padding:4px 22px}

/* Hero */
.hero{left:0;top:82px;width:1200px;height:368px;background:radial-gradient(ellipse at 40% 40%,#1d5ab4 0%,#0f3a86 45%,var(--navy-deep) 100%)}
.hero-visual{left:130px;top:44px;width:470px;height:322px;border-radius:18px 18px 6px 6px;background:linear-gradient(160deg,#3a3f47 0%,#1b1e24 55%,#c9ccd1 100%)}
.hero-copy{left:616px;top:94px;color:var(--white)}
.hero-kicker{font-size:20px;font-weight:300}
.hero-title{font-weight:300;font-size:38px;line-height:40px;color:var(--sky);margin-top:4px;letter-spacing:-0.5px}
.hero-sub{font-weight:300;font-size:30px;line-height:34px;color:var(--white);letter-spacing:-0.3px}
.hero-text{font-size:11.5px;line-height:18px;color:#bfe4fb;margin-top:10px;width:470px}
.btn-orange{display:inline-block;background:var(--orange);color:var(--white);font-family:"Oswald",sans-serif;font-size:14px;padding:6px 16px;border-radius:3px;margin-top:18px}

/* Register band */
.register-band{left:0;top:450px;width:1200px;height:108px;background:linear-gradient(180deg,var(--orange) 0%,var(--orange-dark) 100%)}
.register-line{left:177px;top:40px;width:620px;white-space:nowrap;font-family:"Lobster",cursive;font-size:19.5px;line-height:26px;color:var(--white)}
.btn-register{left:815px;top:32px;width:203px;height:43px;border-radius:22px;background:var(--navy);border:2px solid #3d6cc0;color:var(--white);font-family:"Oswald",sans-serif;font-size:16px;display:flex;align-items:center;justify-content:center}

/* About */
.about{left:0;top:558px;width:1200px;height:475px;background:var(--paper)}
.section-title{font-family:"Oswald",sans-serif;font-weight:400;color:var(--navy)}
.about-title{left:177px;top:38px;font-size:32px}
.about-body{left:177px;top:96px;width:364px;font-size:11px;line-height:16px;color:var(--grey)}
.about-body .lead{font-size:12.5px;line-height:18px;color:#3b3f46;margin-bottom:14px}
.about-body p{margin-bottom:14px}
.features{left:588px;top:46px;width:430px}
.feature{display:flex;gap:18px;height:106px}
.feature-icon{width:72px;height:72px;border-radius:50%;background:var(--navy);flex:none;display:flex;align-items:center;justify-content:center}
.feature h3{font-family:"Oswald",sans-serif;font-weight:400;font-size:15px;color:var(--navy);margin-top:6px}
.feature p{font-size:10.5px;line-height:15px;color:var(--grey);margin-top:4px}

/* Gallery */
.gallery{left:0;top:1033px;width:1200px;height:664px;background:linear-gradient(180deg,#c7ccd4 0%,#9aa5b6 35%,#d9dce2 60%,#7e8ca3 100%)}
.gallery-title{left:0;top:18px;width:1200px;text-align:center;font-size:30px}
.gallery-card{width:267px;height:255px;background:#2e2f33}
.gallery-shot{left:0;top:0;width:267px;height:170px}
.gallery-caption{left:0;top:170px;width:267px;height:85px;background:rgba(40,42,48,.82);padding:14px 16px;color:var(--white)}
.gallery-caption h4{font-family:"Oswald",sans-serif;font-weight:400;font-size:14px}
.gallery-caption p{font-size:10.5px;line-height:14px;margin-top:6px;color:#e5e7ea}

/* Testimonials */
.testimonials{left:0;top:1697px;width:1200px;height:199px;background:var(--white)}
.testimonials-pointer{left:588px;top:-14px}
.testimonials-title{left:0;top:14px;width:1200px;text-align:center;font-family:"Lobster",cursive;font-size:30px;color:var(--navy)}
.quote-card{width:413px;height:114px;background:#eeeeee;padding:14px 18px 0 78px}
.quote-avatar{left:18px;top:14px;width:48px;height:48px;border-radius:50%;background:linear-gradient(160deg,#b9a08a,#5b4a3d)}
.quote-card p{font-size:10.5px;line-height:14px;color:var(--grey)}
.quote-author{text-align:right;font-size:10.5px;color:var(--ink);margin-top:6px;line-height:13px}
.quote-author span{display:block;color:var(--orange)}

/* Footer */
.site-footer{left:0;top:1896px;width:1200px;height:244px;background:linear-gradient(120deg,#0a2a66 0%,#072055 55%,#0f3b88 100%)}
.footer-col{top:48px;color:var(--white)}
.footer-col h5{font-family:"Oswald",sans-serif;font-weight:400;font-size:14px;margin-bottom:10px}
.footer-col li{list-style:none;font-size:10.5px;line-height:17px;color:#a9c5ef}
.footer-col .blurb{font-size:10.5px;line-height:15px;color:#a9c5ef;width:265px}
.subscribe-input{width:264px;height:24px;background:var(--white);margin-top:10px;border-radius:2px}
.btn-subscribe{display:block;margin:11px 0 0 171px;width:93px;height:28px;background:var(--orange);font-family:"Oswald",sans-serif;font-size:12px;color:var(--white);text-align:center;line-height:28px;border-radius:2px}
.legal-bar{left:0;top:2140px;width:1200px;height:22px;background:var(--navy-deep);color:#a9c5ef;font-size:10px;line-height:22px}
.legal-copy{left:177px;top:0}
.legal-links{right:176px;top:0;display:flex;gap:12px}
</style>
</head>
<body>

<header class="site-header abs">
  <div class="brand abs"><span class="brand-mark"></span><span class="brand-name">Kelvora</span></div>
  <nav class="main-nav abs">
    <a class="active">HOME</a><a>FEATURES</a><a>PRICING</a><a>ABOUT US</a><a>SHOWCASE</a><a>CONTACT US</a>
  </nav>
</header>

<section class="hero abs">
  <div class="hero-visual abs" role="img" aria-label="Laptop showing a sample online store beside an iced milkshake glass"></div>
  <div class="hero-copy abs">
    <p class="hero-kicker">Our firm's mission is to listen to clients</p>
    <h1 class="hero-title">EVERYTHING YOU NEED TO</h1>
    <h2 class="hero-sub">CREATE A SUCESSFUL ONLINE STORE</h2>
    <p class="hero-text">24/7 monitoring system monitoring every role on every server and desktop.<br>Proactively fixing problems before the users know there is an issue.</p>
    <span class="btn-orange">VIEW DETAILS</span>
  </div>
</section>

<section class="register-band abs">
  <p class="register-line abs">Start building powerful, professional, easy to use websites and online stores</p>
  <span class="btn-register abs">CLICK TO REGISTER HERE</span>
</section>

<section class="about abs">
  <h2 class="section-title about-title abs">ABOUT US</h2>
  <div class="about-body abs">
    <p class="lead">Sed ut perspiciatis unde omnis iste natus error sit voluptatem accusantium doloremque laudantium, totam rem aperiam, eaque ipsa quae ab illo inventore veritatis et quasi architecto beatae vitae dicta sunt explicabo.</p>
    <p>Neque porro quisquam est, qui dolorem ipsum quia dolor sit amet, consectetur, adipisci velit, sed quia non numquam eius modi tempora incidunt ut labore et dolore magnam aliquam quaerat voluptatem. Ut enim ad minima veniam, quis nostrum exercitationem ullam corporis suscipit laboriosam, nisi ut aliquid ex ea commodi consequatur.</p>
    <p>Sed ut perspiciatis unde omnis iste natus error sit voluptatem accusantium doloremque laudantium, totam rem aperiam, eaque ipsa quae ab illo inventore veritatis et quasi architecto beatae vitae dicta sunt explicabo. Nemo enim ipsam voluptatem quia voluptas sit aspernatur aut odit aut fugit, sed quia consequuntur magni dolores eos qui ratione voluptatem sequi nesciunt. Neque porro quisquam est, qui dolorem ipsum quia dolor sit amet, consectetur, adipisci velit, sed quia non numquam eius modi tempora incidunt ut labore et dolore magnam aliquam quaerat voluptatem. Ut enim ad minima veniam, quis nostrum exercitationem ullam corporis suscipit laboriosam, nisi ut aliquid ex ea commodi consequatur.</p>
  </div>
  <div class="features abs">
    <div class="feature">
      <div class="feature-icon"><svg width="36" height="30" viewBox="0 0 36 30" fill="none" stroke="#fff" stroke-width="2.5"><rect x="2" y="2" width="32" height="20" rx="2"/><path d="M12 28h12M18 22v6"/><path d="M9 8l5 5M9 13V8h5" stroke-width="2"/></svg></div>
      <div><h3>EASY TO USE &amp; FLEXIBLE</h3><p>Sed ut perspiciatis unde omnis iste natus error sit voluptatem accusantium doloremque laudantium, totam rem aperiam, eaque ipsa quae ab illo inventore veritatis et quasi architecto beatae vitae dicta sunt explicabo.</p></div>
    </div>
    <div class="feature">
      <div class="feature-icon"><svg width="38" height="32" viewBox="0 0 38 32" fill="none" stroke="#fff" stroke-width="2.5"><path d="M12 12l7-9 7 9"/><path d="M2 12h34l-4 18H6z"/><path d="M12 17v8M19 17v8M26 17v8" stroke-width="2"/></svg></div>
      <div><h3>POWERFUL ECOMMERCE</h3><p>Sed ut perspiciatis unde omnis iste natus error sit voluptatem accusantium doloremque laudantium, totam rem aperiam, eaque ipsa quae ab illo inventore veritatis et quasi architecto beatae vitae dicta sunt explicabo.</p></div>
    </div>
    <div class="feature">
      <div class="feature-icon"><svg width="34" height="34" viewBox="0 0 34 34" fill="#fff"><path d="M17 2l4.4 9.6 10.4 1.1-7.8 7 2.2 10.3L17 24.8 7.8 30l2.2-10.3-7.8-7 10.4-1.1z"/></svg></div>
      <div><h3>AMAZING DESIGNS</h3><p>Sed ut perspiciatis unde omnis iste natus error sit voluptatem accusantium doloremque laudantium, totam rem aperiam, eaque ipsa quae ab illo inventore veritatis et quasi architecto beatae vitae dicta sunt explicabo.</p></div>
    </div>
    <div class="feature">
      <div class="feature-icon"><svg width="38" height="32" viewBox="0 0 38 32" fill="none" stroke="#fff" stroke-width="2.5"><path d="M2 6h12l3 4h19v20H2z"/><circle cx="22" cy="21" r="5" stroke-width="2"/><path d="M26 25l5 4" stroke-width="2"/></svg></div>
      <div><h3>PACKED WITH FEATURES</h3><p>Sed ut perspiciatis unde omnis iste natus error sit voluptatem accusantium doloremque laudantium, totam rem aperiam, eaque ipsa quae ab illo inventore veritatis et quasi architecto beatae vitae dicta sunt explicabo.</p></div>
    </div>
  </div>
</section>

<section class="gallery abs" role="img" aria-label="Blurred sky and cloud backdrop">
  <h2 class="section-title gallery-title abs">OUR GALLERY</h2>

  <div class="gallery-card abs" style="left:177px;top:80px">
    <div class="gallery-shot abs" role="img" aria-label="Website shown on a desktop monitor" style="background:linear-gradient(150deg,#222 0%,#6b4a2a 60%,#2a2a2a 100%)"></div>
    <div class="gallery-caption abs"><h4>QUIS AUTEM VEL EUM</h4><p>vel illum qui dolorem eum fugiat quo voluptas nulla pariatur</p></div>
  </div>
  <div class="gallery-card abs" style="left:467px;top:80px">
    <div class="gallery-shot abs" role="img" aria-label="Colourful cupcakes on a table" style="background:linear-gradient(150deg,#4aa4d6 0%,#d98aa8 50%,#7a4b3a 100%)"></div>
    <div class="gallery-caption abs"><h4>QUIS AUTEM VEL EUM</h4><p>vel illum qui dolorem eum fugiat quo voluptas nulla pariatur</p></div>
  </div>
  <div class="gallery-card abs" style="left:759px;top:80px">
    <div class="gallery-shot abs" role="img" aria-label="Tablet displaying a web page" style="background:linear-gradient(150deg,#6f7f73 0%,#c9d3d8 55%,#3c4a52 100%)"></div>
    <div class="gallery-caption abs"><h4>QUIS AUTEM VEL EUM</h4><p>vel illum qui dolorem eum fugiat quo voluptas nulla pariatur</p></div>
  </div>
  <div class="gallery-card abs" style="left:177px;top:361px">
    <div class="gallery-shot abs" role="img" aria-label="Web page with a green banner on a screen" style="background:linear-gradient(150deg,#dfe4e8 0%,#8cc63f 55%,#2d4a2a 100%)"></div>
    <div class="gallery-caption abs"><h4>QUIS AUTEM VEL EUM</h4><p>vel illum qui dolorem eum fugiat quo voluptas nulla pariatur</p></div>
  </div>
  <div class="gallery-card abs" style="left:467px;top:361px">
    <div class="gallery-shot abs" role="img" aria-label="Laptop screen showing a social profile page" style="background:linear-gradient(150deg,#1b1d22 0%,#e7eaf0 55%,#3c5a8a 100%)"></div>
    <div class="gallery-caption abs"><h4>QUIS AUTEM VEL EUM</h4><p>vel illum qui dolorem eum fugiat quo voluptas nulla pariatur</p></div>
  </div>
  <div class="gallery-card abs" style="left:759px;top:361px">
    <div class="gallery-shot abs" role="img" aria-label="Hand holding a phone with an event page" style="background:linear-gradient(150deg,#9aa0a6 0%,#2a6f8f 50%,#c7b9a6 100%)"></div>
    <div class="gallery-caption abs"><h4>QUIS AUTEM VEL EUM</h4><p>vel illum qui dolorem eum fugiat quo voluptas nulla pariatur</p></div>
  </div>
</section>

<section class="testimonials abs">
  <svg class="testimonials-pointer abs" width="24" height="14" viewBox="0 0 24 14"><path d="M0 14L12 0l12 14z" fill="#fff"/></svg>
  <h2 class="testimonials-title abs">Our Client Testimonials</h2>
  <div class="quote-card abs" style="left:177px;top:65px">
    <div class="quote-avatar abs" role="img" aria-label="Client portrait"></div>
    <p>Sed ut perspiciatis unde omnis iste natus error sit voluptatem accusantium doloremque laudantium, totam rem aperiam, eaque ipsa quae ab illo inventore veritatis et quasi architecto beatae vitae dicta sunt explicabo.</p>
    <p class="quote-author">Marcus Delane<span>USA</span></p>
  </div>
  <div class="quote-card abs" style="left:610px;top:65px">
    <div class="quote-avatar abs" role="img" aria-label="Client portrait"></div>
    <p>Sed ut perspiciatis unde omnis iste natus error sit voluptatem accusantium doloremque laudantium, totam rem aperiam, eaque ipsa quae ab illo inventore veritatis et quasi architecto beatae vitae dicta sunt explicabo.</p>
    <p class="quote-author">Marcus Delane<span>USA</span></p>
  </div>
</section>

<footer class="site-footer abs">
  <div class="footer-col abs" style="left:177px"><h5>PRODUCT</h5><ul><li>About Us</li><li>Our Blog</li><li>Pricing</li><li>Our Themes</li><li>Features</li><li>Terms and Conditions</li></ul></div>
  <div class="footer-col abs" style="left:329px"><h5>MARKETPLACE</h5><ul><li>Support Forum</li><li>Documentation</li><li>FAQ</li><li>Customization</li><li>Installation Service</li><li>Video Tutorials</li><li>Support Policy</li><li>Contact Us</li></ul></div>
  <div class="footer-col abs" style="left:489px"><h5>SUPPORT</h5><ul><li>Showcase</li><li>Press</li><li>Partners</li><li>Hosting</li><li>Affiliates</li><li>Promotions</li><li>Features</li></ul></div>
  <div class="footer-col abs" style="left:625px"><h5>ABOUT US</h5><ul><li>News</li><li>New Themes</li><li>Contests</li><li>Theme Concepts</li><li>Freebies</li><li>Highlight</li><li>Promotions</li><li>Tips &amp; Advice</li></ul></div>
  <div class="footer-col abs" style="left:759px"><h5>GET IN TOUCH WITH US</h5>
    <p class="blurb">We would love to hear about you, be part of our community come join us, we will have so much fun! We have all kinds of gifts and cool stuff for you!</p>
    <div class="subscribe-input"></div>
    <span class="btn-subscribe">SUBSCRIBE</span>
  </div>
</footer>

<div class="legal-bar abs">
  <span class="legal-copy abs">Copyright © 2013 - Kelvora.com Premium Themes - All rights reserved.</span>
  <span class="legal-links abs"><span>Home</span><span>Features</span><span>Terms &amp; Conditions</span><span>FAQ</span><span>Contact</span></span>
</div>

</body>
</html>
```